International Water Business Needs a Label Design for Energy Drinks (Can)

We need a label design for a new product launch, specifically in the Energy Drinks segment. We want to communicate that is fresh, and give a premium, imported feel to the product. The product will be competing with local energy drink products in China as well as with ZapFalcon. The product will be imported into China.

The specifications of the can is in the uploaded PDF file.

The mother brand name is "Dorvelin Springs". The file is attached here as well.

* if you require the vector file of the logo, please let me know and I will send it to your email.
Updates

Dear designers,

If you require the vector file of the logo, please let me know your email and i will send it to you.

Thanks very much.

Warm regards,

Ros

Dear designers,

In addition to the current designs that you are working on, I was thinking making the background Mimo-Tuka Red with my brand "Dorvelin Springs" in white. Something to work on as well?

Thanks very much.

Ros

Dear Designers,

Also I would like something simple and eye catching and classy at the same time. I would prefer not to have gimicky symbols in the middle of the label. 

Thanks very much for your efforts and looking forward to all your designs.

Regards,

Ros

Dear all,

The limit for the colours on the design is 6. Thanks very much.

Ros 

Target Market(s)

Target market to be for 20-30 year olds who lead active and sometimes stressful lifestyles.

Industry/Entity Type

Business

```html
<!DOCTYPE html>
<html lang="en">
<head>
<meta charset="utf-8">
<title>Dorvelin Springs Energy Drink – Can Label</title>
<link rel="stylesheet" href="https://fonts.googleapis.com/css2?family=Abril+Fatface&family=Orbitron:wght@700&family=Oswald:wght@500&display=swap">
<style>
  :root {
    --page-bg: #e4e4e6;
    --label-edge: #5a1450;
    --label-deep: #8a1a6e;
    --label-magenta: #e0187e;
    --label-bright: #f5479e;
    --ink-white: #ffffff;
  }
  html, body {
    margin: 0;
    padding: 0;
    width: 1200px;
    height: 1200px;
    overflow: hidden;
    background: var(--page-bg);
  }
  .canvas {
    position: relative;
    width: 1200px;
    height: 1200px;
  }
  .can-label {
    position: absolute;
    left: 80px;
    top: 395px;
    width: 1040px;
    height: 410px;
    display: block;
  }
  .brand-name {
    font-family: "Abril Fatface", serif;
    fill: var(--ink-white);
  }
  .energy-tag {
    font-family: "Orbitron", sans-serif;
    font-weight: 700;
    fill: var(--ink-white);
    letter-spacing: 2px;
  }
  .volume {
    font-family: "Oswald", sans-serif;
    font-weight: 500;
    fill: var(--ink-white);
  }
  .trademark {
    font-family: "Oswald", sans-serif;
    fill: var(--ink-white);
  }
  .tag-rule { stroke: var(--ink-white); stroke-width: 3; }
</style>
</head>
<body>
<main class="canvas">
  <svg class="can-label" viewBox="0 0 900 355" xmlns="http://www.w3.org/2000/svg" aria-label="Dorvelin Springs energy drink can label">
    <defs>
      <linearGradient id="label-colour" x1="0" y1="0" x2="1" y2="0">
        <stop offset="0" stop-color="var(--label-edge)"/>
        <stop offset="0.18" stop-color="var(--label-deep)"/>
        <stop offset="0.35" stop-color="var(--label-magenta)"/>
        <stop offset="0.55" stop-color="var(--label-bright)"/>
        <stop offset="0.8" stop-color="var(--label-magenta)"/>
        <stop offset="1" stop-color="var(--label-edge)"/>
      </linearGradient>
      <linearGradient id="label-sheen" x1="0" y1="0" x2="0" y2="1">
        <stop offset="0" stop-color="#ffffff" stop-opacity="0.18"/>
        <stop offset="0.45" stop-color="#ffffff" stop-opacity="0"/>
        <stop offset="1" stop-color="#3a0a30" stop-opacity="0.25"/>
      </linearGradient>
      <linearGradient id="decor-tone" x1="0" y1="0" x2="1" y2="1">
        <stop offset="0" stop-color="#ffffff" stop-opacity="0.10"/>
        <stop offset="1" stop-color="#ffffff" stop-opacity="0.22"/>
      </linearGradient>
    </defs>

    <rect class="label-base" x="0" y="0" width="900" height="355" fill="url(#label-colour)"/>
    <rect class="label-sheen" x="0" y="0" width="900" height="355" fill="url(#label-sheen)"/>

    <rect class="decor-area" x="0" y="290" width="900" height="65" fill="url(#decor-tone)"
          role="img" aria-label="White decorative swoosh sweeping across the lower part of the label"/>

    <g class="energy-tag-group">
      <line class="tag-rule" x1="250" y1="66" x2="305" y2="66"/>
      <text class="energy-tag" x="490" y="66" font-size="28" text-anchor="middle">ENERGY DRINK</text>
      <line class="tag-rule" x1="675" y1="66" x2="730" y2="66"/>
    </g>

    <text class="brand-name" x="480" y="165" font-size="100" text-anchor="middle">Dorvelin</text>
    <text class="brand-name" x="560" y="270" font-size="100" text-anchor="middle">Springs</text>
    <text class="trademark" x="725" y="290" font-size="14">TM</text>

    <text class="volume" x="40" y="220" font-size="24" transform="rotate(-90 40 220)" text-anchor="middle">250ml</text>
  </svg>
</main>
</body>
</html>
```